Business Card Design Project

We have a logo, but would like to expand the use of it into a business card design. We are a B2B technology exchange platform for institutional investors to invest excess cash into short term assets matching their credit and pricing parameters. The assets are fractionalized and investors invest in portions.

Our customers are large, institutional, financial companies who are a bit traditional. We are high energy rebels with a cause...we are a disruptive technology and want to be viewed as a game changer but we need to present an image of trustworthiness and secure.

We are open not only to the image design but the material, die cut, etc. but want to stay in the traditional size of a business card.

We have other formats of the logo if needed. Our website is www.brambleharbor.com
Updates

I have posted a powerpoint template that we have been using.  This should not be considered the template we will use (after business cards we will have another project to incorporate business card design into powerpoint template) but just to give you a flavor of where we have been and have used in the past.

Target Market(s)

Institutional investors, asset managers, large fund institutions

Industry/Entity Type

Financial

Requirements
Must have
• Our logo
Traditional size
Nice to have
• unique use of logo, unique material, die cut, etc
Crisp, clean look
Use of both sides of card in a creative manner

```html
<!DOCTYPE html>
<html lang="en">
<head>
<meta charset="utf-8">
<title>Bramble Harbor – Business Card</title>
<link rel="stylesheet" href="https://fonts.googleapis.com/css2?family=Arimo:wght@400;700&family=Tinos:wght@400;700&display=swap">
<style>
  :root {
    --sky-top: #65646c;
    --sky-mid: #b4b4b8;
    --sky-low: #e2e2e2;
    --brand-orange: #f7941d;
    --swoosh-red: #ff5a0a;
    --glow: rgba(255, 120, 40, 0.55);
    --ink-gray: #5b5b60;
    --logo-gray: #636366;
    --name-cream: #fff7bf;
    --line-white: #ffffff;
  }
  * { margin: 0; padding: 0; box-sizing: border-box; }
  html, body {
    width: 1200px;
    height: 693px;
    overflow: hidden;
    background: #ffffff;
  }
  .card {
    position: relative;
    width: 1200px;
    height: 693px;
    overflow: hidden;
    background: linear-gradient(to bottom, var(--sky-top) 0%, var(--sky-mid) 28%, var(--sky-low) 60%, var(--sky-low) 100%);
  }
  .card-waves {
    position: absolute;
    inset: 0;
    width: 1200px;
    height: 693px;
  }
  .holder {
    position: absolute;
    top: 86px;
    left: 0;
    width: 1212px;
    text-align: center;
    font-family: "Arimo", Arial, sans-serif;
    color: var(--name-cream);
  }
  .holder-name {
    font-size: 45px;
    font-weight: 700;
    letter-spacing: 1px;
    line-height: 1.1;
  }
  .holder-role {
    font-size: 31px;
    font-weight: 400;
    margin-top: 6px;
  }
  .brand {
    position: absolute;
    left: 58px;
    top: 268px;
    display: flex;
    align-items: center;
    gap: 22px;
    font-family: "Arimo", Arial, sans-serif;
    font-weight: 700;
    color: var(--logo-gray);
  }
  .brand-name {
    font-size: 64px;
    line-height: 0.95;
    letter-spacing: 1px;
  }
  .brand-dot {
    width: 92px;
    height: 92px;
    border-radius: 50%;
    background: var(--brand-orange);
    flex: none;
  }
  .contact {
    position: absolute;
    left: 612px;
    top: 488px;
    width: 520px;
    text-align: center;
    font-family: "Tinos", "Times New Roman", serif;
    color: var(--ink-gray);
  }
  .contact-tel {
    font-size: 45px;
    font-weight: 700;
    line-height: 1.2;
  }
  .contact-line {
    font-size: 29px;
    line-height: 1.3;
  }
</style>
</head>
<body>
  <div class="card">
    <svg class="card-waves" viewBox="0 0 1200 693" aria-hidden="true">
      <defs>
        <filter id="wave-glow" x="-10%" y="-50%" width="120%" height="200%">
          <feGaussianBlur stdDeviation="14"/>
        </filter>
      </defs>
      <path d="M0,452 C100,480 250,495 340,490 C520,480 700,400 900,405 C1050,408 1150,425 1200,430 L1200,470 L0,500 Z"
            fill="var(--glow)" filter="url(#wave-glow)"/>
      <path class="wave-fill" d="M0,452 C100,480 250,495 340,490 C520,480 700,400 900,405 C1050,408 1150,425 1200,430 L1200,693 L0,693 Z"
            fill="var(--brand-orange)"/>
      <path class="wave-swoosh" d="M0,378 C40,440 150,482 340,490 C200,486 60,462 0,425 Z"
            fill="var(--swoosh-red)"/>
      <path class="wave-line" d="M0,452 C100,480 250,495 340,490 C520,480 700,400 900,405 C1050,408 1150,425 1200,430"
            fill="none" stroke="var(--line-white)" stroke-width="3"/>
      <path class="wave-line-inner" d="M0,378 C40,440 150,482 340,490"
            fill="none" stroke="var(--line-white)" stroke-width="2"/>
    </svg>

    <header class="holder">
      <h1 class="holder-name">RAE T. SOLANO</h1>
      <p class="holder-role">Graphic Designer</p>
    </header>

    <div class="brand">
      <span class="brand-name">BRAMBLE<br>HARBOR</span>
      <span class="brand-dot"></span>
    </div>

    <address class="contact" style="font-style: normal;">
      <p class="contact-tel">Tel: 0987-654-321-0</p>
      <p class="contact-line">Email: www.brambleharbor.com</p>
      <p class="contact-line">Website: www.brambleharbor.com</p>
    </address>
  </div>
</body>
</html>
```